Ad Design for a child care centre

Bright Pebbles Child Care Centre offers a safe, nurturing environment where your child will get the attention and care that he or she needs. Our ratio of children to adults is always within state guidelines - and often even higher - to make certain each child receives top-quality care
We are also state licensed as a Child Care facility and have met or exceeded all health and safety guidelines.
3-5 year Kinder Funded Program
Story Time
Show and Tell
Puzzles and Games
Computer Time
Arts and Crafts
Music
Pre-Reading Activities
And much more
You can rest assured that your child will be cared for with the most kindness, love and respect. We believe all children are precious gifts and we treat them as though they are our own.
Full-time, part-time, Half days, Before, after-school schedules are available.
To learn more, contact us today! 03 9481 -0576 or info@brightpebbles.example.au

```html
<!DOCTYPE html>
<html lang="en">
<head>
<meta charset="utf-8">
<title>Bright Pebbles Child Care and Kinder – Flyer</title>
<link rel="stylesheet" href="https://fonts.googleapis.com/css2?family=Ubuntu:wght@400;500;700&display=swap">
<style>
  :root {
    --teal: #3b9089;
    --teal-deep: #2f8a82;
    --coral: #f26b5f;
    --red: #d4493b;
    --orange: #f0a54f;
    --yellow: #f1d67c;
    --sky: #bfe3f3;
    --white: #ffffff;
    --ink: #333333;
    --phone-red: #c8202f;
    --photo-warm: #d9b79a;
    --photo-green: #8aa56a;
    --photo-grey-a: #6f6f6f;
    --photo-grey-b: #b5b5b5;
  }
  * { box-sizing: border-box; margin: 0; padding: 0; }
  html, body { width: 988px; height: 1200px; overflow: hidden; background: var(--white); }
  body { font-family: "Ubuntu", sans-serif; color: var(--ink); position: relative; }

  .tile-grid {
    position: absolute; left: 0; top: 0; width: 988px; height: 360px;
    display: grid; grid-template-columns: repeat(5, 1fr); grid-template-rows: repeat(2, 1fr);
  }
  .tile--teal { background: var(--teal); }
  .tile--coral { background: var(--coral); }
  .tile--orange { background: var(--orange); }
  .tile--red { background: var(--red); }
  .tile--yellow { background: var(--yellow); }
  .tile--photo { background: radial-gradient(circle at 50% 45%, var(--photo-warm), #a98f7a 75%); }
  .tile--photo-green { background: radial-gradient(circle at 55% 50%, var(--photo-warm), var(--photo-green) 80%); }

  .group-photo {
    position: absolute; left: 0; top: 366px; width: 988px; height: 282px;
    background: linear-gradient(135deg, var(--photo-grey-b), var(--photo-grey-a) 60%, #8c8c8c);
  }

  .brand-badge {
    position: absolute; left: 40px; top: 360px; width: 400px; height: 320px;
    border-radius: 50% 50% 50% 50% / 60% 60% 40% 40%;
    background: var(--white);
    display: flex; flex-direction: column; align-items: center; justify-content: center;
    text-align: center; padding: 30px 40px 10px;
  }
  .brand-name {
    font-weight: 700; font-size: 46px; line-height: 1.08; color: #6a3d8f;
  }
  .brand-tagline {
    margin-top: 16px; font-size: 21px; line-height: 1.3; color: var(--ink);
  }

  .intro {
    position: absolute; left: 0; top: 648px; width: 590px; height: 222px;
    background: var(--teal); color: var(--white);
    font-weight: 500; font-size: 17.5px; line-height: 1.38;
    padding: 28px 28px 0 36px;
  }
  .program {
    position: absolute; left: 590px; top: 648px; width: 398px; height: 222px;
    background: var(--coral); color: var(--white);
    font-weight: 500; font-size: 16.5px; line-height: 1.3;
    padding: 22px 24px 0 24px;
  }
  .program-title { font-weight: 700; }
  .program-list { list-style: none; }
  .program-list li::before { content: "• "; }

  .assurance {
    position: absolute; left: 0; top: 870px; width: 988px; height: 200px;
    background: var(--sky);
  }
  .assurance-col {
    position: absolute; top: 40px; font-size: 15.5px; line-height: 1.38; color: var(--ink);
  }
  .assurance-col--left { left: 40px; width: 400px; top: 66px; }
  .assurance-col--right { left: 500px; width: 440px; top: 36px; }
  .assurance-divider {
    position: absolute; left: 470px; top: 36px; width: 1px; height: 110px; background: var(--ink);
  }
  .schedule {
    position: absolute; left: 0; top: 160px; width: 988px; text-align: center;
    font-size: 19px; color: var(--ink);
  }

  .contact {
    position: absolute; left: 0; top: 1070px; width: 988px; height: 130px; background: var(--white);
  }
  .contact-cta {
    position: absolute; left: 60px; top: 22px; width: 420px; text-align: center;
    font-weight: 700; font-size: 33px; line-height: 1.2; color: var(--teal-deep);
  }
  .contact-details { position: absolute; left: 520px; top: 4px; width: 440px; text-align: center; }
  .contact-phone { font-weight: 700; font-size: 44px; color: var(--phone-red); letter-spacing: 1px; }
  .contact-email, .contact-web { font-size: 19px; color: var(--ink); letter-spacing: 1px; margin-top: 6px; }
</style>
</head>
<body>
  <section class="tile-grid">
    <div class="tile tile--teal"></div>
    <div class="tile tile--photo" role="img" aria-label="Photo of a smiling toddler in a cap"></div>
    <div class="tile tile--coral"></div>
    <div class="tile tile--photo" role="img" aria-label="Photo of a laughing baby indoors"></div>
    <div class="tile tile--orange"></div>
    <div class="tile tile--photo-green" role="img" aria-label="Photo of a baby outdoors"></div>
    <div class="tile tile--red"></div>
    <div class="tile tile--photo" role="img" aria-label="Photo of a baby girl wearing a tiara"></div>
    <div class="tile tile--yellow"></div>
    <div class="tile tile--photo" role="img" aria-label="Photo of a child with face paint"></div>
  </section>

  <div class="group-photo" role="img" aria-label="Black and white photo of children sitting in a circle on the floor"></div>

  <div class="brand-badge">
    <div class="brand-name">Bright Pebbles Child Care and Kinder</div>
    <p class="brand-tagline">We are not just a child Care<br>Centre we are Family</p>
  </div>

  <p class="intro">Bright Pebbles Child Care Centre offers a safe, nurturing environment where your child will get the attention and care that he or she needs. Our ratio of children to adults is always within state guidelines - and often even higher - to make certain each child receives top-quality care</p>

  <div class="program">
    <p class="program-title">3-5 year Kinder Funded Program</p>
    <ul class="program-list">
      <li>Show and Tell</li>
      <li>Puzzles and Games</li>
      <li>Computer Time</li>
      <li>Arts and Crafts</li>
      <li>Music</li>
      <li>Pre-Reading Activities</li>
      <li>And much more</li>
    </ul>
  </div>

  <section class="assurance">
    <p class="assurance-col assurance-col--left">We are also state licensed as a Child Care facility and have met or exceeded all health and safety guidelines.</p>
    <div class="assurance-divider"></div>
    <p class="assurance-col assurance-col--right">You can rest assured that your child will be cared for with the most kindness, love and respect. We believe all children are precious gifts and we treat them as though they are our own.</p>
    <p class="schedule">Full-time, part-time, Half days, Before, after-school schedules are available.</p>
  </section>

  <section class="contact">
    <p class="contact-cta">To learn more<br>contact us today!</p>
    <div class="contact-details">
      <p class="contact-phone">03 9481 -0576</p>
      <p class="contact-email">or info@brightpebbles.example.au</p>
      <p class="contact-web">www.brightpebbles.example.au</p>
    </div>
  </section>
</body>
</html>
```